Asphalt Paving Specialists Business Cards

Our company is TREVIN ASPHALT. We need a business cards two of our asphalt paving team members. We're asphalt specialists.
I need two made up please. The details on the front of the each business card i would like please is as follows.
Address is 87 Marrowby St, Clontarf, QLD, 4019.

Company Director
Gordon Pelliway
gord@trevinpave.com.au
04 58 736 042
www.trevinpave.com.au

Supervisor
Curtis Vonnegard
curtis@trevinpave.com.au
0462 873 105
www.trevinpave.com.au

We do all aspects of Asphalt Paving. Specific Services include - Driveways, Carparks & sub-divisions. All Roads. Repairs and Maintenance.

We provide free quotes!

I dont have a certain way i want them to look so im open to all designs :)

** I have uploaded our logo for the TREVIN ASPHALT. HOWEVER, CAN YOU PLEASE GET RID OF THE ( PTY LTD )

Thank you
Renata Fulch
TREVIN ASPHALT

Target Market(s)

Home owners and Business Owners

Contact Information for Business Card

Asphalt Paving Specialists. All aspects of Asphalt. Residential, Commercial & Industrial. Based in Brisbane.

Font styles to use
Sans Serif

Colors

Designer to choose colors to be used in the design.

Requirements
Nice to have
• maybe an image of a driveway? or Asphalt?

```html
<!DOCTYPE html>
<html lang="en">
<head>
<meta charset="utf-8">
<title>Trevin Asphalt – Business Cards</title>
<link href="https://fonts.googleapis.com/css2?family=Open+Sans:wght@400;600;700&display=swap" rel="stylesheet">
<style>
  :root {
    --page-bg: #2b2b2d;
    --card-black: #050505;
    --card-white: #ffffff;
    --brand-blue: #1aaee8;
    --brand-blue-light: #8fd8f6;
    --ink: #111111;
    --text-light: #ffffff;
    --rule: #8a8a8a;
  }
  * { box-sizing: border-box; margin: 0; padding: 0; }
  html, body { width: 1200px; height: 885px; overflow: hidden; }
  body {
    background: var(--page-bg);
    font-family: "Open Sans", Arial, sans-serif;
    position: relative;
  }
  .card {
    position: absolute;
    width: 600px;
    height: 343px;
    overflow: hidden;
    box-shadow: 0 10px 30px rgba(0,0,0,0.5);
  }

  /* Back card */
  .card-back {
    left: 90px; top: 100px;
    background: var(--card-black);
    color: var(--text-light);
    text-align: center;
  }
  .back-brand {
    position: absolute; top: 70px; left: 0; right: 0;
    display: flex; align-items: center; justify-content: center; gap: 14px;
    font-weight: 700; font-size: 34px; letter-spacing: 2px;
  }
  .brand-dot {
    width: 18px; height: 18px; border-radius: 50%;
    background: var(--text-light);
  }
  .back-tagline {
    position: absolute; top: 180px; left: 0; right: 0;
    font-size: 15px;
  }
  .back-rule {
    position: absolute; left: 50%; transform: translateX(-50%);
    height: 1px; background: linear-gradient(90deg, transparent, var(--rule), transparent);
  }
  .back-rule.upper { top: 206px; width: 260px; }
  .back-rule.lower { top: 238px; width: 520px; }
  .back-subhead {
    position: absolute; top: 210px; left: 0; right: 0;
    font-size: 15px;
  }
  .back-services {
    position: absolute; top: 250px; left: 0; right: 0;
    font-size: 15px;
  }

  /* Front card */
  .card-front {
    left: 510px; top: 440px;
    background: var(--card-white);
  }
  .front-band { position: absolute; inset: 0; }
  .front-brand {
    position: absolute; top: 88px; left: 0; right: 0;
    display: flex; align-items: center; justify-content: center; gap: 12px;
    font-weight: 700; font-size: 36px; letter-spacing: 2px;
    color: var(--ink);
  }
  .front-brand .brand-dot { background: var(--brand-blue); }
  .contact-list {
    position: absolute; top: 222px; right: 34px;
    list-style: none;
    color: var(--text-light);
    font-size: 14px; line-height: 21px;
  }
  .contact-list li { display: flex; align-items: center; gap: 8px; }
  .contact-list svg { width: 13px; height: 13px; flex: none; }
  .person {
    position: absolute; left: 34px; bottom: 26px;
    color: var(--text-light);
  }
  .person-name { font-weight: 700; font-size: 22px; line-height: 26px; }
  .person-role { font-size: 15px; letter-spacing: 0.5px; }
</style>
</head>
<body>

<section class="card card-back" aria-label="Business card back">
  <div class="back-brand"><span class="brand-dot"></span>TREVIN ASPHALT</div>
  <p class="back-tagline">We do all aspects of Asphalt Paving.</p>
  <div class="back-rule upper"></div>
  <p class="back-subhead">Specific Services</p>
  <div class="back-rule lower"></div>
  <p class="back-services">Driveways • Carparks &amp; sub-divisions • All Roads • Repairs &amp; Maintenance.</p>
</section>

<section class="card card-front" aria-label="Business card front">
  <svg class="front-band" viewBox="0 0 600 343" width="600" height="343">
    <defs>
      <radialGradient id="bandGlow" cx="0.62" cy="0.55" r="0.6">
        <stop offset="0" stop-color="var(--brand-blue-light)"/>
        <stop offset="1" stop-color="var(--brand-blue)"/>
      </radialGradient>
    </defs>
    <polygon points="0,276 600,190 600,343 0,343" fill="url(#bandGlow)"/>
    <polygon points="0,262 600,176 600,192 0,278" fill="#0c0c0c"/>
    <line x1="0" y1="270" x2="600" y2="184" stroke="#ffffff" stroke-width="3" stroke-dasharray="22 16"/>
  </svg>

  <div class="front-brand"><span class="brand-dot"></span>TREVIN ASPHALT</div>

  <ul class="contact-list">
    <li>
      <svg viewBox="0 0 16 16"><path fill="#fff" d="M3 1h3l1.5 4-2 1.3a9 9 0 0 0 4.2 4.2L11 8.5l4 1.5v3a2 2 0 0 1-2 2A12 12 0 0 1 1 3a2 2 0 0 1 2-2z"/></svg>
      04 58 736 042
    </li>
    <li>
      <svg viewBox="0 0 16 16"><rect x="1" y="3" width="14" height="10" fill="#fff"/><path d="M1 3l7 6 7-6" fill="none" stroke="#1aaee8" stroke-width="1.5"/></svg>
      gord@trevinpave.com.au
    </li>
    <li>
      <svg viewBox="0 0 16 16"><circle cx="8" cy="8" r="7" fill="#fff"/><path d="M1 8h14M8 1c-3 4-3 10 0 14M8 1c3 4 3 10 0 14" fill="none" stroke="#1aaee8" stroke-width="1.2"/></svg>
      www.trevinpave.com.au
    </li>
  </ul>

  <div class="person">
    <p class="person-name">Gordon Pelliway</p>
    <p class="person-role">COMPANY DIRECTOR</p>
  </div>
</section>

</body>
</html>
```